Harborvale Ventures brochure for Investment partnership, young harold pembly

We need a brochure design to attract new investors for our investing partnership Called Harborvale Ventures. We are based in New Orleans, La. We primarily invest in stocks, bonds, and crypto but venture out into other categories as well. We would like to see designs with the black and gold like our logo. The final design should say new, fresh, sleek, tech, and honorable. BROUCHURE WILL BE 4 pages.or one folded sheet a paparer if that makes sense.
Updates

A chart showing Harborvale Ventures gains since 2019 28.6 percent and the TR 400 gAINS 7.1 PERCENT

Target Market(s)

Probable Investors

Industry/Entity Type

Financial Planning

Colors

Designer to choose only greyscale colors for use in the design.

Requirements
Must have
• Black and Gold accent. Stock market feel. Sleek, High tech, innovative, Intellgent design.
Nice to have
• Page colors possibly black.
Should not have
• Boring, Old school,

```html
<!DOCTYPE html>
<html lang="en">
<head>
<meta charset="utf-8">
<title>Harborvale Ventures – Brochure Proposal</title>
<link rel="stylesheet" href="https://fonts.googleapis.com/css2?family=Cinzel:wght@600;700&family=Playfair+Display:ital,wght@1,600&family=Montserrat:wght@400;600;700;800&display=swap">
<style>
  :root {
    --canvas: #e9e9e9;
    --page: #0d0d0d;
    --panel: #1b1b1b;
    --gold: #d8b23a;
    --gold-light: #f1d77a;
    --gold-dark: #9c7a1c;
    --text: #e6e6e6;
    --muted: #a9a9a9;
    --label: #7a7a7a;
    --bar-grey: #6a6a6a;
  }
  * { box-sizing: border-box; margin: 0; padding: 0; }
  html, body { width: 882px; height: 1200px; overflow: hidden; }
  body {
    background: var(--canvas);
    font-family: "Montserrat", sans-serif;
    color: var(--text);
    position: relative;
  }
  .proposal-label {
    position: absolute; top: 22px; left: 0; width: 100%;
    text-align: center; font-size: 11px; font-weight: 600;
    letter-spacing: 2px; color: var(--label);
  }
  .page {
    position: absolute; width: 330px; height: 485px;
    background: var(--page); overflow: hidden;
    box-shadow: 0 4px 14px rgba(0,0,0,.25);
  }
  .page--cover { left: 100px; top: 56px; }
  .page--intro { left: 452px; top: 56px; }
  .page--how { left: 100px; top: 598px; }
  .page--about { left: 452px; top: 598px; }

  .photo { position: absolute; }
  .curve { position: absolute; left: 0; width: 330px; }

  .brand {
    font-family: "Cinzel", serif; font-weight: 700;
    color: var(--gold); text-align: center; text-transform: uppercase;
    line-height: 1;
  }
  .brand-sub { display: block; margin-top: 4px; }

  /* Cover */
  .cover-brand { position: absolute; top: 22px; left: 0; width: 100%; font-size: 24px; letter-spacing: 1px; }
  .cover-brand .brand-sub { font-size: 13px; letter-spacing: 4px; }
  .cover-photo { top: 76px; left: 0; width: 330px; height: 250px;
    background: linear-gradient(180deg,#8d8d8d 0%,#5c5c5c 55%,#2e2e2e 100%); }
  .cover-tagline { position: absolute; top: 356px; left: 30px; width: 270px;
    text-align: center; font-size: 8.5px; font-weight: 700; line-height: 1.5;
    color: var(--gold-light); text-transform: uppercase; }
  .cover-bar { position: absolute; top: 398px; left: 0; width: 330px; height: 66px;
    background: linear-gradient(90deg,var(--gold-dark),var(--gold),var(--gold-light),var(--gold));
    color: #111; text-align: center; font-weight: 800; text-transform: uppercase;
    padding-top: 12px; font-size: 18px; line-height: 1.1; }

  /* Intro */
  .intro-heading { position: absolute; top: 16px; left: 0; width: 100%; text-align: center;
    font-family: "Playfair Display", serif; font-style: italic; font-weight: 600;
    font-size: 19px; color: var(--gold); }
  .intro-lead { position: absolute; top: 48px; left: 40px; width: 250px; text-align: center;
    font-size: 8px; line-height: 1.5; color: var(--muted); }
  .intro-photo { top: 86px; left: 0; width: 330px; height: 210px;
    background: linear-gradient(180deg,#bdbdbd 0%,#8a8a8a 60%,#4a4a4a 100%); }
  .intro-you { position: absolute; top: 320px; left: 0; width: 100%; text-align: center;
    font-size: 24px; font-weight: 800; color: var(--gold); letter-spacing: 1px; }
  .intro-points { position: absolute; top: 356px; left: 40px; width: 250px; text-align: center;
    font-size: 8.5px; line-height: 1.6; color: var(--text); list-style: none; }
  .intro-market { position: absolute; top: 408px; left: 0; width: 100%; text-align: center;
    font-size: 18px; font-weight: 800; color: var(--gold); }
  .intro-brand { position: absolute; top: 446px; left: 0; width: 100%; font-size: 14px; }

  /* How it works */
  .how-photo { top: 0; left: 0; width: 330px; height: 170px;
    background: linear-gradient(135deg,#4f4f4f 0%,#2a2a2a 60%,#151515 100%); }
  .how-title { position: absolute; top: 16px; left: 120px; font-size: 19px; font-weight: 800;
    color: var(--gold); letter-spacing: .5px; }
  .steps { position: absolute; top: 196px; left: 22px; width: 286px; list-style: none; }
  .step { display: flex; gap: 10px; margin-bottom: 12px; }
  .step-icon { flex: 0 0 22px; height: 22px; border-radius: 50%; background: var(--gold);
    display: flex; align-items: center; justify-content: center; }
  .step-title { font-size: 8.5px; font-weight: 700; color: var(--gold); margin-bottom: 3px; }
  .step-text { font-size: 7.5px; line-height: 1.5; color: var(--muted); }
  .gains-chart { position: absolute; top: 330px; left: 22px; width: 286px; height: 112px;
    background: var(--panel); border-top: 2px solid var(--gold); }
  .how-brand { position: absolute; top: 456px; left: 0; width: 100%; font-size: 13px; }

  /* About */
  .about-photo { top: 0; left: 0; width: 330px; height: 270px;
    background: linear-gradient(135deg,#6e5a2a 0%,#3a3020 45%,#1a1610 100%); }
  .about-brand { position: absolute; top: 112px; left: 0; width: 100%; font-size: 28px; color: var(--gold-light); }
  .about-brand .brand-sub { font-size: 14px; letter-spacing: 5px; margin-top: 8px; }
  .about-title { position: absolute; top: 304px; left: 20px; width: 290px; text-align: center;
    font-size: 12px; font-weight: 800; color: var(--gold); text-transform: uppercase; line-height: 1.3; }
  .about-text { position: absolute; top: 346px; left: 28px; width: 274px; text-align: center;
    font-size: 7.5px; line-height: 1.6; color: var(--muted); }
  .about-footer { position: absolute; top: 440px; left: 20px; width: 290px; display: flex;
    align-items: center; justify-content: center; gap: 12px; }
  .about-footer .brand { font-size: 11px; }
  .footer-bar { background: var(--gold); color: #111; font-size: 7.5px; font-weight: 700;
    padding: 4px 10px; letter-spacing: 1px; }
</style>
</head>
<body>
  <div class="proposal-label"># PROPOSAL 1</div>

  <section class="page page--cover">
    <div class="brand cover-brand">Harborvale<span class="brand-sub">Ventures</span></div>
    <div class="photo cover-photo" role="img" aria-label="Black and white photo of a New Orleans streetcar on a palm-lined avenue"></div>
    <svg class="curve" style="top:300px" height="60" viewBox="0 0 330 60">
      <path d="M0 30 Q165 -5 330 30 L330 60 L0 60 Z" fill="#0d0d0d"/>
      <path d="M0 30 Q165 -5 330 30" fill="none" stroke="#d8b23a" stroke-width="4"/>
    </svg>
    <p class="cover-tagline">Become a partner &amp; build generational wealth<br>by investing in the stock market</p>
    <div class="cover-bar">A first of its kind<br>investment club</div>
  </section>

  <section class="page page--intro">
    <h2 class="intro-heading">If you are receiving this brochure...</h2>
    <p class="intro-lead">My purpose is simple: to invite people who want to put their money to work.</p>
    <div class="photo intro-photo" role="img" aria-label="Black and white photo of a smiling group of young professionals"></div>
    <svg class="curve" style="top:262px" height="50" viewBox="0 0 330 50">
      <path d="M0 40 Q165 0 330 20 L330 50 L0 50 Z" fill="#0d0d0d"/>
      <path d="M0 40 Q165 0 330 20" fill="none" stroke="#d8b23a" stroke-width="4"/>
    </svg>
    <h3 class="intro-you">YOU ARE</h3>
    <ul class="intro-points">
      <li>someone who wants to build real generational wealth</li>
      <li>Not Fear schemes</li>
      <li>But through the greatest wealth builder available</li>
    </ul>
    <h3 class="intro-market">THE STOCK MARKET</h3>
    <div class="brand intro-brand">Harborvale Ventures</div>
  </section>

  <section class="page page--how">
    <div class="photo how-photo" role="img" aria-label="Photo of a trader wearing a headset in front of stock chart screens"></div>
    <h2 class="how-title">HOW IT WORKS</h2>
    <svg class="curve" style="top:150px" height="40" viewBox="0 0 330 40">
      <path d="M0 10 Q165 40 330 10 L330 40 L0 40 Z" fill="#0d0d0d"/>
      <path d="M0 10 Q165 40 330 10" fill="none" stroke="#d8b23a" stroke-width="3"/>
    </svg>
    <ul class="steps">
      <li class="step">
        <span class="step-icon"><svg width="12" height="12" viewBox="0 0 12 12"><path d="M2 6 L5 9 L10 3" stroke="#111" stroke-width="2" fill="none"/></svg></span>
        <div><div class="step-title">Make Initial Deposit</div><p class="step-text">Partners fund an account and join the pool with a clear agreement.</p></div>
      </li>
      <li class="step">
        <span class="step-icon"><svg width="12" height="12" viewBox="0 0 12 12"><path d="M2 6 L5 9 L10 3" stroke="#111" stroke-width="2" fill="none"/></svg></span>
        <div><div class="step-title">Share in the Capital Pool</div><p class="step-text">Your deposit joins the pool and gains are split by the share each partner holds in the fund.</p></div>
      </li>
      <li class="step">
        <span class="step-icon"><svg width="12" height="12" viewBox="0 0 12 12"><path d="M2 6 L5 9 L10 3" stroke="#111" stroke-width="2" fill="none"/></svg></span>
        <div><div class="step-title">Track Every Result</div><p class="step-text">Monthly reports show every position, gain and fee in plain terms.</p></div>
      </li>
    </ul>
    <svg class="gains-chart" viewBox="0 0 286 112" role="img" aria-label="Bar chart: Harborvale Ventures gains since 2019 28.6 percent, TR 400 gains 7.1 percent">
      <text x="14" y="20" font-family="Montserrat, sans-serif" font-size="9" font-weight="800" fill="#d8b23a" letter-spacing="1">GAINS SINCE 2019</text>
      <line x1="14" y1="30" x2="272" y2="30" stroke="#333" stroke-width="1"/>
      <text x="14" y="46" font-family="Montserrat, sans-serif" font-size="7.5" font-weight="700" fill="#e6e6e6">HARBORVALE VENTURES</text>
      <rect x="14" y="51" width="208" height="14" fill="#d8b23a"/>
      <text x="228" y="62" font-family="Montserrat, sans-serif" font-size="10" font-weight="800" fill="#f1d77a">28.6%</text>
      <text x="14" y="82" font-family="Montserrat, sans-serif" font-size="7.5" font-weight="700" fill="#e6e6e6">TR 400</text>
      <rect x="14" y="87" width="52" height="14" fill="#6a6a6a"/>
      <text x="72" y="98" font-family="Montserrat, sans-serif" font-size="10" font-weight="800" fill="#a9a9a9">7.1%</text>
    </svg>
    <div class="brand how-brand">Harborvale Ventures</div>
  </section>

  <section class="page page--about">
    <div class="photo about-photo" role="img" aria-label="Photo of a fountain pen on gold textured paper"></div>
    <div class="brand about-brand">Harborvale<span class="brand-sub">Ventures</span></div>
    <svg class="curve" style="top:244px" height="40" viewBox="0 0 330 40">
      <path d="M0 26 Q165 0 330 26 L330 40 L0 40 Z" fill="#0d0d0d"/>
      <path d="M0 26 Q165 0 330 26" fill="none" stroke="#d8b23a" stroke-width="3"/>
    </svg>
    <h2 class="about-title">About Harborvale Ventures<br>and General Partner</h2>
    <p class="about-text">Harborvale Ventures was founded in 2019 by a New Orleans investor with a long record in the stock market. The general partner manages stocks, bonds and crypto with a steady and honest approach, placing partner interests first in every decision.</p>
    <div class="about-footer">
      <div class="brand">Harborvale Ventures</div>
      <div class="footer-bar">INVEST WITH PURPOSE</div>
    </div>
  </section>
</body>
</html>
```